Brochure for a six month Life Transformation program for executives

I need a A4 brochure that will be physically printed out to give to prospective clients for a six month coaching, life transformation program. I have included here a video link that discusses the brief in detail.
https://www.vidtrellis.com/share/4b81e2f09c3d47a6b52e18d0a7f3c915

I've uploaded a file with logos and photos to include as well as a outline of each page.
Updates

Here is an updated video to show you what I'm liking what I don't like https://www.vidtrellis.com/share/e92d07b1a6f84c3098d5b7c1f4a26e08

Target Market(s)

35 - 55 male executives

Industry/Entity Type

Life Coaching

Requirements
Must have
• All the information in the outline
Nice to have
• icons, vector diagrams, the theme of transformation and revolution

```html
<!DOCTYPE html>
<html lang="en">
<head>
<meta charset="utf-8">
<title>Prime Renewal – Program Brochure</title>
<link href="https://fonts.googleapis.com/css2?family=Arimo:ital,wght@0,400;0,700;1,700&family=Open+Sans:wght@400&display=swap" rel="stylesheet">
<style>
:root{
  --stage:#6f7074;
  --brand-blue:#0e4d93;
  --deep-blue:#253e7c;
  --accent-red:#c4403a;
  --paper:#ffffff;
  --ink:#333333;
  --muted:#a9a9a9;
  --rule:#1a4b93;
  --soft:#eef0f3;
}
*{box-sizing:border-box;margin:0;padding:0}
html,body{width:886px;height:1200px;overflow:hidden}
body{background:var(--stage);font-family:"Arimo",Arial,sans-serif;color:var(--ink);position:relative}
.page{position:absolute;width:369px;height:522px;background:var(--paper);overflow:hidden}
.page--cover{left:67px;top:67px;background:var(--brand-blue)}
.page--credentials{left:450px;top:67px;background:linear-gradient(125deg,#fff 40%,var(--soft) 62%,#fff 80%,var(--soft))}
.page--program{left:67px;top:610px}
.page--problem{left:450px;top:610px}
.abs{position:absolute}

/* cover */
.cover__shadow{position:absolute;inset:0}
.cover__frame{position:absolute;left:57px;top:138px;width:254px;height:236px;border:4px solid var(--paper)}
.cover__mark{position:absolute;left:144px;top:92px;width:46px;height:46px;background:var(--paper)}
.cover__name{position:absolute;left:0;width:369px;top:200px;text-align:center;color:var(--paper);font-size:12px;letter-spacing:2.6px;font-weight:400}
.cover__pillars{position:absolute;left:98px;top:256px;list-style:none;color:var(--paper);font-size:21px;line-height:27px}
.cover__pillars li::before{content:"• "}
.cover__tagline{position:absolute;left:50px;width:269px;top:441px;text-align:center;color:var(--paper);font-family:"Open Sans",Arial,sans-serif;font-size:8px;line-height:10.5px}

/* shared header */
.header-rule{position:absolute;height:1.5px;background:var(--rule);top:40px}
.header-name{position:absolute;top:31px;right:14px;font-size:8px;font-weight:700;color:var(--brand-blue)}

/* credentials */
.cred__col{position:absolute;left:0;width:184px;background:var(--brand-blue)}
.cred__text{position:absolute;left:33px;width:150px;color:var(--paper);font-weight:700;font-size:9.4px;line-height:12px}
.cred__rule{position:absolute;left:185px;width:167px;height:1.5px;background:var(--rule)}
.cred__highlight{position:absolute;left:0;width:369px;top:192px;text-align:center;font-style:italic;font-weight:700;font-size:12.6px;line-height:14.8px;color:var(--muted);padding:0 55px}
.badge{position:absolute;background:#d9dbe0;border-radius:3px}
.client-names{position:absolute;left:197px;width:150px;font-size:8.5px;line-height:13px;color:#222;font-weight:700}
.circle-dot{display:inline-block;width:14px;height:14px;border-radius:50%;background:#222;vertical-align:middle;margin-right:5px}

/* program page */
.intro-band{position:absolute;left:0;top:99px;width:175px;height:118px;background:var(--brand-blue);color:var(--paper)}
.intro-band h2{position:absolute;left:27px;top:16px;font-size:10px;line-height:12px;font-weight:700}
.intro-band p{position:absolute;left:27px;top:49px;width:120px;font-size:8.6px;line-height:10.4px}
.wheel{position:absolute;left:156px;top:53px}
.section-title{position:absolute;left:27px;font-size:8.5px;font-weight:700;color:var(--brand-blue)}
.small-copy{position:absolute;left:27px;width:316px;font-size:5.6px;line-height:7.4px}
.benefit{position:absolute;top:398px;height:67px;background:var(--brand-blue);color:var(--paper);text-align:center;font-size:7px;line-height:8.8px;padding-top:22px}
.benefit strong{display:block}
.benefit__icon{position:absolute;top:370px;width:44px;height:44px;border-radius:50%;background:var(--paper);border:2px solid var(--brand-blue)}
.vision{position:absolute;left:35px;top:475px;width:300px;font-size:5.6px;line-height:7.4px}

/* problem page */
.body-copy{position:absolute;left:24px;width:321px;font-size:7px;line-height:9px;text-align:justify}
.question-panel{position:absolute;left:20px;top:288px;width:334px;height:106px;background:var(--brand-blue);border-radius:0 12px 140px 0/0 12px 96px 0;overflow:hidden}
.question-mark{position:absolute;left:-2px;top:-2px;font-size:92px;font-weight:700;color:#3f6fb0;line-height:1}
.question-list{position:absolute;left:33px;top:21px;list-style:none;color:var(--paper);font-size:8.5px;line-height:12.9px}
</style>
</head>
<body>

<!-- Cover -->
<section class="page page--cover">
  <svg class="cover__shadow" width="369" height="522" aria-hidden="true">
    <polygon points="311,138 369,171 369,502 69,374 311,374" fill="var(--deep-blue)"/>
  </svg>
  <div class="cover__frame" style="background:var(--brand-blue)"></div>
  <div class="cover__mark"></div>
  <div class="cover__name">PRIME RENEWAL</div>
  <ul class="cover__pillars">
    <li>Your Life</li>
    <li>Your Potential</li>
    <li>Your Revolution</li>
  </ul>
  <p class="cover__tagline">A six month life transformation program for overworked executives to restore life balance through health and fitness optimization while maintaining their high functioning career.</p>
</section>

<!-- Credentials -->
<section class="page page--credentials">
  <div class="cred__col" style="top:0;height:175px"></div>
  <div class="cred__col" style="top:263px;height:259px"></div>
  <div class="header-rule" style="left:184px;width:126px"></div>
  <div class="header-name">Prime Renewal</div>

  <p class="cred__text" style="top:107px">Internationally educated with multiple qualifications from Australia and Canada</p>
  <div class="badge" style="left:199px;top:103px;width:44px;height:14px"></div>
  <div class="badge" style="left:248px;top:103px;width:44px;height:14px"></div>
  <div class="badge" style="left:297px;top:103px;width:38px;height:20px;background:#e5b3b0"></div>
  <div class="badge" style="left:203px;top:126px;width:92px;height:14px;border-radius:7px"></div>
  <div class="cred__rule" style="top:153px"></div>

  <p class="cred__highlight">OVER 15 YEARS EXPERIENCE, WORKING DIRECTLY WITH 100S OF CLIENTS AND FACILITATED WELL OVER 1000 FITNESS CLASSES</p>

  <p class="cred__text" style="top:301px">We work with executives clients from companies like</p>
  <div class="client-names" style="top:290px">Northvale Spirits · Aerlune<br>Maple Broadcast · Orchard Devices</div>
  <div class="cred__rule" style="top:338px"></div>

  <p class="cred__text" style="top:352px">In 2016 selected to represent Toronto as an Elite Trainer to provide coaching services for Global Coach Circle</p>
  <div class="client-names" style="top:362px;font-size:9.5px"><span class="circle-dot"></span>Global Coach Circle</div>
  <div class="cred__rule" style="top:403px"></div>

  <p class="cred__text" style="top:430px">Featured on CityPulse Blog, Horizon News, Trailhead Magazine</p>
  <div class="client-names" style="top:430px;font-size:9.5px">CityPulse Blog · Horizon News<br>Trailhead Magazine</div>
  <div class="cred__rule" style="top:469px"></div>
</section>

<!-- Program -->
<section class="page page--program">
  <div class="header-rule" style="left:14px;width:300px"></div>
  <div class="header-name">Prime Renewal</div>

  <div class="intro-band">
    <h2>WHAT IS A PRIME<br>RENEWAL?</h2>
    <p>A Prime Renewal - is to overthrow your old regimes and bad habits and become your true potential self, a version that is fit, healthy, confident and successful.</p>
  </div>
  <svg class="wheel" width="207" height="207" role="img" aria-label="Renewal wheel illustration: raised fist inside a ring of steps for discipline, nutrition, exercise, clarity and measurement">
    <defs>
      <radialGradient id="wheelTone">
        <stop offset="0" stop-color="var(--accent-red)"/>
        <stop offset="0.6" stop-color="var(--brand-blue)"/>
        <stop offset="0.85" stop-color="#c9cbd0"/>
        <stop offset="1" stop-color="var(--accent-red)"/>
      </radialGradient>
    </defs>
    <circle cx="103.5" cy="103.5" r="103" fill="url(#wheelTone)"/>
  </svg>

  <h3 class="section-title" style="top:243px">THE PROGRAM IN BRIEF</h3>
  <p class="small-copy" style="top:263px">A six month life transformation program for overworked executives to restore life balance through health and fitness optimization while maintaining their high functioning career. A combination of 1:1 coaching, workshops, live events, workouts and accountability groups creates a unique learning environment and an immersive experience for our clients to experience a Prime Renewal.</p>

  <h3 class="section-title" style="top:301px">WHO IT'S FOR</h3>
  <p class="small-copy" style="top:321px">High performing Individuals who have focused on their career and other aspects of their life while neglecting their health and fitness.<br>Executives and Business Leaders who want to optimise their life through enhancing their health and fitness</p>
  <p class="small-copy" style="top:355px">Self Employed Entrepreneurs who understand in order to achieve your potential you need accountability and a community of like minded people.</p>

  <div class="benefit" style="left:29px;width:94px"><strong>Peak Physical Performance</strong>be pain free and functionally fit.</div>
  <div class="benefit" style="left:128px;width:112px"><strong>Physical Confidence</strong>we get you to not only look good, feel good, but love what you see in the mirror.</div>
  <div class="benefit" style="left:246px;width:94px"><strong>Be in Control</strong>of all aspects of your life, professionally and personally.</div>
  <div class="benefit__icon" role="img" aria-label="Strength icon" style="left:54px"></div>
  <div class="benefit__icon" role="img" aria-label="Confident figure icon" style="left:162px"></div>
  <div class="benefit__icon" role="img" aria-label="Control sliders icon" style="left:271px"></div>

  <p class="vision">We envision a world where people move past focusing on financial gains at the cost of their physical and mental health. One where all aspects of their life are truly balanced and they gain fulfillment through living a healthy, fit and confident life.</p>
</section>

<!-- Problem -->
<section class="page page--problem">
  <div class="header-rule" style="left:14px;width:300px"></div>
  <div class="header-name">Prime Renewal</div>

  <p class="body-copy" style="top:95px">In this modern world, most people struggle finding the balance between maintaining a high functional career and their body's health and fitness at the same time. Often by the time they realise this, it's too late, the damage of a neglected self has been done. The longer it's left unattended, the harder it becomes to reverse and impact on other aspects of their life becomes more and more noticeable.</p>
  <p class="body-copy" style="top:150px">Poor Physical Health - if you're a high performing professional you're likely leading a more sedentary life than you would like to be. Aches, pains, low energy, being overweight and prone to injury are all too common. Over time and distance, your health can't help but suffer.</p>
  <p class="body-copy" style="top:185px">Poor Body Confidence - As much as you would refuse to admit it, when health and fitness hasn't been at the top of your priority list, your boardroom boldness doesn't match how you see yourself in the mirror. That lack of confidence away from your office could be holding you back in more ways than you realise.</p>
  <p class="body-copy" style="top:230px">Poor Personal Health Routines - Lacking the personal accountability to workout and eat properly means you have no structured plans which incorporate optimized nutrition and exercise into your weekly routine. Without a proper routine you're unable to live the quality of life you deserve.</p>

  <div class="question-panel">
    <span class="question-mark" aria-hidden="true">?</span>
    <ul class="question-list">
      <li>What is the cost to your personal life for not looking after yourself?</li>
      <li>What does your future look like if you continue on this path?</li>
      <li>Are you currently more likely to get sick or injured?</li>
      <li>Are you setting a good example for your kids?</li>
      <li>Are you in the relationship of your dreams?</li>
    </ul>
  </div>

  <p class="body-copy" style="top:431px;text-align:left">These are many of the questions that people find themselves asking when those problems are left unchecked.</p>
  <p class="body-copy" style="top:459px;text-align:left">"Acknowledge the pain you're causing by not looking after yourself, only then will your reasons for permanent change become clear."</p>
</section>

</body>
</html>
```